Store Front Signage for an Upscale Cake & Dessert Bakery

We need a design for store front windows. We are a 12 year old bakery specializing in cakes, cupcakes, cookies, pies, and other desserts. We recently moved to a high traffic location.. and we would like to boost our visual presence; we can be seen from the main road but are competing with other businesses for attention. Attached is a photo of our store front with posters but this signage will be for window film for the entire window span. (see the store front to the left of the photo to see the green and yellow as a film example)
Our logo and store sign (not like in photo, that is showing more red) are in shades of pink. The most visible part of the signage is in the upper third to upper half of the 60" panels.
The signs in the window currently say Life's Short. Eat Cake.
We now use Enjoy Life. Eat Cake.
The design should span all the windows and door -- this can be individual panels or one design that covers all panels. I have pink and greys chosen but please DO NOT let this constrain you. The inside of the bakery has grey floors and walls. white cabinetry, black granite countertops. The only thing with color is the baked goods and display cakes, pictures of cakes, the logo and menu and employee shirts.

Target Market(s)

we are located at a busy intersection --- we would like to capture the attention of people in cars as they pass by and entice them to stop in

Font styles to use
Serif
Sans Serif

Colors
d3d3d3
757575
ffffff
e24197
e667a6
eea4c8
f9d9e8

Requirements
Must have
• I would like the design to be easily discernible at the road way that is about 75 feet from store front. If you look at the photos I provide, note that the font size that is easily readable from the road are the ones in the top panes (although the shadow from the building makes them difficult to see -- the best visibility is the top 1/3 of the 60" panels.
Nice to have
• would like to have some non-photo graphics of a cake ( like a birthday cake), tiered cake, cupcakes, and cookies or pie for the panels --- but DO NOT let this constrain you. I need something to grab attention while cars are stopped at the nearby traffic light.
• If this design works well... I will be changing the panel on a seasonal basis
Should not have
• words that cannot be read from a distance.

```html
<!DOCTYPE html>
<html lang="en">
<head>
<meta charset="utf-8">
<title>Window Film – Bakery Store Front</title>
<link rel="stylesheet" href="https://fonts.googleapis.com/css2?family=Merriweather:wght@700;900&family=Yesteryear&family=Montserrat:wght@700&display=swap">
<style>
  :root {
    --frame: #1c1718;
    --pink-hot: #e24197;
    --pink-mid: #e667a6;
    --pink-soft: #eea4c8;
    --pink-pale: #f9d9e8;
    --plum: #8e2a5c;
    --plum-deep: #6e1f45;
    --white: #ffffff;
    --grey-light: #d3d3d3;
    --grey: #757575;
  }
  * { box-sizing: border-box; margin: 0; padding: 0; }
  html, body { width: 1200px; height: 1200px; overflow: hidden; background: var(--white); }
  .storefront { position: relative; width: 1200px; height: 1200px; }
  .frame { position: absolute; left: 40px; top: 329px; width: 1120px; height: 542px; background: var(--frame); }
  .pane { position: absolute; overflow: hidden; }
  .pane--top { background: linear-gradient(180deg, #e985b8 0%, var(--pink-mid) 35%, var(--pink-hot) 60%, #eb8fc0 85%, var(--pink-soft) 100%); }
  .pane--mid { background: linear-gradient(180deg, #ec99c6 0%, var(--pink-mid) 45%, var(--pink-hot) 100%); }
  .pane--low { background: linear-gradient(180deg, #e4509f 0%, var(--pink-hot) 100%); }
  .lace { position: absolute; background: linear-gradient(90deg, #e9e3e6, #f6f2f4 50%, #e9e3e6); opacity: .9; }
  .slogan {
    position: absolute; transform: translate(-50%, -50%);
    font-family: "Merriweather", Georgia, serif; font-weight: 900; font-size: 56px;
    color: var(--pink-pale); text-shadow: 3px 3px 0 var(--plum); white-space: nowrap;
  }
  .menu {
    position: absolute; transform: translateX(-50%); text-align: center;
    font-family: "Merriweather", Georgia, serif; font-weight: 900; font-size: 24px;
    line-height: 43.6px; color: var(--pink-pale); text-shadow: 2px 2px 0 var(--plum); white-space: nowrap;
  }
  .band { position: absolute; background: var(--pink-pale); opacity: .85; }
  .art { position: absolute; border-radius: 10px; }
  .open-sign {
    position: absolute; left: 514px; top: 329px; width: 171px; height: 143px;
    background: repeating-linear-gradient(90deg, #c7457f 0 14px, #d86699 14px 28px);
  }
  .open-sign__word {
    position: absolute; left: 50%; top: 52px; transform: translate(-50%, -50%) rotate(-6deg);
    font-family: "Yesteryear", cursive; font-size: 70px; color: var(--plum-deep);
    text-shadow: 0 0 12px var(--pink-pale), 0 0 4px var(--white); white-space: nowrap;
  }
  .open-sign__num {
    position: absolute; left: 50%; top: 110px; transform: translate(-50%, -50%);
    font-family: "Merriweather", Georgia, serif; font-weight: 700; font-size: 20px;
    color: var(--plum-deep); text-shadow: 0 0 6px var(--white);
  }
  .door { position: absolute; left: 528px; top: 495px; width: 144px; height: 341px; background: var(--pink-hot); }
  .door__stripes {
    position: absolute; left: 0; top: 104px; width: 144px; height: 191px;
    background: repeating-linear-gradient(90deg, #a8376c 0 14px, #c05a8a 14px 28px);
    box-shadow: inset 0 8px 10px rgba(0,0,0,.25), inset 0 -8px 10px rgba(0,0,0,.25);
  }
  .brand {
    position: absolute; left: 0; top: 48px; width: 144px; text-align: center;
    font-family: "Merriweather", Georgia, serif; font-weight: 700; font-size: 13px;
    color: var(--plum-deep); line-height: 16px;
  }
  .brand__mark { display: inline-block; width: 8px; height: 8px; background: var(--plum-deep); border-radius: 50%; margin-right: 4px; vertical-align: middle; }
  .welcome {
    position: absolute; left: 50%; transform: translateX(-50%); text-align: center;
    font-family: "Yesteryear", cursive; font-size: 44px; line-height: 48px;
    color: var(--pink-pale); text-shadow: 2px 2px 0 var(--plum-deep); white-space: nowrap;
  }
</style>
</head>
<body>
<main class="storefront">
  <div class="frame"></div>

  <!-- top row -->
  <div class="pane pane--top" style="left:40px;top:329px;width:228px;height:143px"></div>
  <div class="pane pane--top" style="left:277px;top:329px;width:228px;height:143px"></div>
  <div class="pane pane--top" style="left:694px;top:329px;width:229px;height:143px"></div>
  <div class="pane pane--top" style="left:932px;top:329px;width:228px;height:143px"></div>

  <!-- middle row -->
  <div class="pane pane--mid" style="left:40px;top:481px;width:228px;height:285px"></div>
  <div class="pane pane--mid" style="left:277px;top:481px;width:228px;height:285px"></div>
  <div class="pane pane--mid" style="left:694px;top:481px;width:229px;height:285px"></div>
  <div class="pane pane--mid" style="left:932px;top:481px;width:228px;height:285px"></div>

  <!-- bottom row -->
  <div class="pane pane--low" style="left:40px;top:776px;width:228px;height:95px"></div>
  <div class="pane pane--low" style="left:277px;top:776px;width:228px;height:95px"></div>
  <div class="pane pane--low" style="left:694px;top:776px;width:229px;height:95px"></div>
  <div class="pane pane--low" style="left:932px;top:776px;width:228px;height:95px"></div>

  <!-- lace trims -->
  <div class="lace" role="img" aria-label="White lace ribbon trim" style="left:460px;top:329px;width:42px;height:542px"></div>
  <div class="lace" role="img" aria-label="White lace ribbon trim" style="left:697px;top:329px;width:42px;height:542px"></div>

  <!-- slogan -->
  <div class="slogan" style="left:149px;top:403px">enjoy</div>
  <div class="slogan" style="left:388px;top:403px">life</div>
  <div class="slogan" style="left:805px;top:403px">eat</div>
  <div class="slogan" style="left:1043px;top:403px">cake</div>

  <!-- open sign -->
  <div class="open-sign">
    <div class="open-sign__word">Open</div>
    <div class="open-sign__num">110</div>
  </div>

  <!-- door -->
  <div class="door">
    <div class="brand"><span class="brand__mark"></span>ROSALIND'S<br>bake shoppe</div>
    <div class="door__stripes"></div>
    <div class="welcome" style="top:150px">Well<br>Come</div>
  </div>

  <!-- left feature pane -->
  <div class="band" style="left:40px;top:624px;width:228px;height:19px"></div>
  <div class="band" style="left:40px;top:666px;width:228px;height:18px"></div>
  <div class="band" style="left:40px;top:705px;width:194px;height:28px;border-radius:0 14px 14px 0"></div>
  <div class="art" role="img" aria-label="Colourful party bunting" style="left:40px;top:484px;width:228px;height:58px;background:linear-gradient(90deg,#c9307f,#2aa6c9,#b52a6f,#2a6fb5,#e24197,#f2b21c);opacity:.7"></div>
  <div class="art" role="img" aria-label="Two-tier pink fondant cake with white flowers" style="left:65px;top:550px;width:168px;height:164px;background:linear-gradient(180deg,#e36fa6,#c23a7c);"></div>

  <!-- right feature pane -->
  <div class="band" style="left:932px;top:624px;width:228px;height:19px"></div>
  <div class="band" style="left:932px;top:666px;width:228px;height:18px"></div>
  <div class="band" style="left:966px;top:705px;width:194px;height:28px;border-radius:14px 0 0 14px"></div>
  <div class="art" role="img" aria-label="Colourful party bunting" style="left:932px;top:484px;width:228px;height:58px;background:linear-gradient(90deg,#f2b21c,#e24197,#2a6fb5,#b52a6f,#2ac0d9,#c9307f);opacity:.7"></div>
  <div class="art" role="img" aria-label="Pink frosted cupcake with cherry and wafer rolls in lace wrapper" style="left:987px;top:553px;width:143px;height:164px;background:linear-gradient(180deg,#f07bb4,#e0a96a);"></div>

  <!-- menus -->
  <div class="menu" style="left:370px;top:513px">Cakes<br>Cupcakes<br>Cokkies<br>Pies &nbsp;&amp;<br>Desserts</div>
  <div class="menu" style="left:827px;top:513px">Custom<br>Cakes<br>-----<br>Holiday<br>Desserts</div>

  <!-- dessert rows -->
  <div class="art" role="img" aria-label="Row of watercolour cake slices, cupcakes and berries" style="left:56px;top:789px;width:192px;height:52px;background:linear-gradient(90deg,#b07a90,#f3b8c8,#e0b070,#c86aa0);opacity:.75"></div>
  <div class="art" role="img" aria-label="Row of watercolour cake slices, cupcakes and berries" style="left:296px;top:789px;width:150px;height:52px;background:linear-gradient(90deg,#b07a90,#f3b8c8,#e0b070);opacity:.75"></div>
  <div class="art" role="img" aria-label="Row of watercolour cupcakes, cake slices and berries" style="left:756px;top:789px;width:150px;height:52px;background:linear-gradient(90deg,#e0b070,#f3b8c8,#b07a90);opacity:.75"></div>
  <div class="art" role="img" aria-label="Row of watercolour cupcakes, cake slices and berries" style="left:952px;top:789px;width:192px;height:52px;background:linear-gradient(90deg,#c86aa0,#e0b070,#f3b8c8,#b07a90);opacity:.75"></div>
</main>
</body>
</html>
```